create clean, simple business card template

using the logo created now we need to create a simple, elegant business card design to suit

Industry/Entity Type

Business

Font styles to use
Other font styles liked:
• segoe ui

Requirements
Must have
• Front:
"Name:"
"Title:"
"Mobile:"
"email:"
and the logo

Back:
Logo
Nice to have
• Text in black but other graphics etc to match colours in logo as provided

```html
<!DOCTYPE html>
<html lang="en">
<head>
<meta charset="utf-8">
<title>K&amp;M Estates – Business Card</title>
<link href="https://fonts.googleapis.com/css2?family=Cinzel:wght@400;600&family=Open+Sans:wght@400;600&display=swap" rel="stylesheet">
<style>
  :root {
    --page-bg: #e6e4e1;
    --card-bg: #ffffff;
    --gold: #8a6a34;
    --ink-dark: #3a3129;
    --text-black: #1f1f1f;
    --rule: #3a3129;
  }
  * { box-sizing: border-box; margin: 0; padding: 0; }
  html, body {
    width: 1200px; height: 873px; overflow: hidden;
    background: var(--page-bg);
  }
  .canvas { position: relative; width: 1200px; height: 873px; }
  .card {
    position: absolute; left: 250px; width: 700px; height: 400px;
    background: var(--card-bg);
    box-shadow: 0 6px 18px rgba(0,0,0,.15);
    overflow: hidden;
  }
  .card--front { top: 24px; }
  .card--back { top: 449px; }

  .brand {
    position: absolute; display: flex; align-items: center; gap: 14px;
    font-family: "Cinzel", serif; font-weight: 400; white-space: nowrap;
  }
  .brand__dot { border-radius: 50%; flex: none; }

  /* front */
  .card--front .brand { left: 60px; top: 128px; font-size: 26px; color: var(--ink-dark); }
  .card--front .brand__dot { width: 22px; height: 22px; background: var(--ink-dark); }
  .divider { position: absolute; width: 2px; background: var(--rule); }
  .card--front .divider { left: 300px; top: 80px; height: 120px; }
  .person { position: absolute; left: 330px; top: 100px; }
  .person__name {
    font-family: "Cinzel", serif; font-weight: 400; font-size: 46px;
    color: var(--gold); line-height: 1.1; white-space: nowrap;
  }
  .person__title {
    font-family: "Open Sans", sans-serif; font-size: 18px;
    letter-spacing: 7px; color: var(--text-black); margin-top: 10px;
  }
  .contact {
    position: absolute; top: 290px; display: flex; align-items: center; gap: 14px;
    font-family: "Open Sans", sans-serif; font-size: 20px; color: var(--text-black);
    white-space: nowrap;
  }
  .contact--phone { left: 60px; }
  .contact--email { left: 330px; }
  .contact svg { width: 28px; height: 28px; flex: none; }

  /* back */
  .band { position: absolute; }
  .band--gold { left: 0; top: 0; width: 10px; height: 250px; background: var(--gold); }
  .band--dark { right: 0; bottom: 0; width: 10px; height: 250px; background: var(--ink-dark); }
  .card--back .brand {
    left: 50%; top: 50%; transform: translate(-50%, -50%);
    font-size: 56px; color: var(--gold); gap: 22px;
  }
  .card--back .brand__dot { width: 40px; height: 40px; background: var(--gold); }
</style>
</head>
<body>
<main class="canvas">
  <section class="card card--front" aria-label="Card front">
    <div class="brand"><span class="brand__dot"></span>K&amp;M Estates</div>
    <div class="divider"></div>
    <div class="person">
      <p class="person__name">John Doe</p>
      <p class="person__title">DIRECTOR</p>
    </div>
    <div class="contact contact--phone">
      <svg viewBox="0 0 28 28" aria-hidden="true">
        <rect x="8" y="3" width="12" height="22" rx="2" fill="none" stroke="var(--ink-dark)" stroke-width="2"/>
        <line x1="12" y1="21" x2="16" y2="21" stroke="var(--ink-dark)" stroke-width="2"/>
      </svg>
      <span>+ 000 00</span>
    </div>
    <div class="contact contact--email">
      <svg viewBox="0 0 28 28" aria-hidden="true">
        <rect x="3" y="7" width="22" height="15" rx="1" fill="none" stroke="var(--ink-dark)" stroke-width="2"/>
        <path d="M3 8 L14 16 L25 8" fill="none" stroke="var(--ink-dark)" stroke-width="2"/>
      </svg>
      <span>km@example.com</span>
    </div>
  </section>

  <section class="card card--back" aria-label="Card back">
    <div class="band band--gold"></div>
    <div class="band band--dark"></div>
    <div class="brand"><span class="brand__dot"></span>K&amp;M Estates</div>
  </section>
</main>
</body>
</html>
```